Vel

I have the logo for the back already. Need the front to match.
Need a VEL logo which I can provide or you can download one - VEL Realty in canada... Back of the card will be my logo and name. Front will have the info...
I would like a black background. Match colors on front to the back..
Details on Card

Target Market(s)

Realestate clients.. Keep it classy like the logo

Contact Information for Business Card

Reena Dhot office - 4035550187 cell - 4035550264 email - Reena@ReenaDhot.Com. website - ReenaDhot.Com Facebook - RDhotRealty Instagram - Reena_Yyc_Realtor Address - 514 - 23 St NE | T3K5M8

Colors
3176b5
33a6d7
85cae6

Requirements
Must have
• same color scheme as the logo
logo will be on the back
Black Background
Horizontal card
The one side of the card should be clean. like I stated, just my logo " Reena Dhot " and nothing else

```html
<!DOCTYPE html>
<html lang="en">
<head>
<meta charset="utf-8">
<title>Reena Dhot – Business Card</title>
<link rel="stylesheet" href="https://fonts.googleapis.com/css2?family=Cormorant+Garamond:wght@600&family=Crimson+Pro:wght@300&display=swap">
<style>
  :root {
    --backdrop: #85cae6;
    --card: #1a1a1a;
    --brand-blue: #1574bb;
    --sky: #85cae6;
    --icon-blue: #3176b5;
    --ink: #e8e8e8;
  }
  html, body {
    margin: 0;
    width: 1200px;
    height: 1200px;
    overflow: hidden;
    background: var(--backdrop);
  }
  .canvas {
    position: relative;
    width: 1200px;
    height: 1200px;
  }
  .card {
    position: absolute;
    left: 239px;
    width: 722px;
    height: 412px;
    background: var(--card);
    box-shadow: 6px 8px 10px rgba(0, 0, 0, 0.28);
  }
  .card--front { top: 155px; }
  .card--back { top: 633px; }

  .front__name {
    position: absolute;
    left: 26px;
    top: 12px;
    margin: 0;
    font-family: "Cormorant Garamond", serif;
    font-weight: 600;
    font-size: 62px;
    letter-spacing: 2px;
    color: var(--sky);
    text-transform: uppercase;
    line-height: 1;
  }
  .front__mark {
    position: absolute;
    right: 28px;
    top: 150px;
    font-family: "Cormorant Garamond", serif;
    font-weight: 600;
    font-size: 50px;
    line-height: 1;
    letter-spacing: 2px;
    color: var(--brand-blue);
    text-transform: uppercase;
    text-align: right;
  }

  .contact {
    font-family: "Crimson Pro", serif;
    font-weight: 300;
    font-size: 19px;
    color: var(--ink);
  }
  .contact__item {
    position: absolute;
    display: flex;
    align-items: center;
    gap: 12px;
    white-space: nowrap;
  }
  .contact__icon {
    width: 16px;
    height: 16px;
    flex: none;
    stroke: var(--icon-blue);
    fill: none;
    stroke-width: 1.3;
  }
  .contact__dot {
    width: 14px;
    height: 14px;
    flex: none;
    border-radius: 3px;
    background: var(--icon-blue);
  }
  .contact__ring {
    width: 13px;
    height: 13px;
    flex: none;
    border-radius: 50%;
    border: 1.5px solid var(--icon-blue);
  }

  .back__name {
    position: absolute;
    left: 0;
    right: 0;
    top: 170px;
    margin: 0;
    text-align: center;
    font-family: "Cormorant Garamond", serif;
    font-weight: 600;
    font-size: 60px;
    letter-spacing: 2px;
    line-height: 1;
    color: var(--brand-blue);
    text-transform: uppercase;
  }
</style>
</head>
<body>
<main class="canvas">

  <section class="card card--front" aria-label="Card front">
    <h1 class="front__name">Reena Dhot</h1>
    <div class="front__mark">Reena<br>Dhot</div>

    <div class="contact">
      <div class="contact__item" style="left:26px; top:254px;">
        <svg class="contact__icon" viewBox="0 0 16 16"><path d="M3 1.5l2.5 0 1 3.5-1.6 1.2a8 8 0 0 0 4.9 4.9L11 9.5l3.5 1v2.5c0 1-1 1.6-2 1.5C6.5 14 2 9.5 1.5 3.5 1.4 2.5 2 1.5 3 1.5z"/></svg>
        <span>4035550187 (Office)</span>
      </div>
      <div class="contact__item" style="left:240px; top:254px;">
        <span>4035550264 (Cell)</span>
      </div>

      <div class="contact__item" style="left:26px; top:291px;">
        <svg class="contact__icon" viewBox="0 0 16 16"><rect x="1" y="3" width="14" height="10"/><path d="M1 3l7 6 7-6M1 13l5-5M15 13l-5-5"/></svg>
        <span>reena@reenadhot.com</span>
      </div>
      <div class="contact__item" style="left:242px; top:291px;">
        <svg class="contact__icon" viewBox="0 0 16 16"><circle cx="8" cy="8" r="7"/><ellipse cx="8" cy="8" rx="3" ry="7"/><path d="M1 8h14M2 4.5h12M2 11.5h12"/></svg>
        <span>reenadhot.com</span>
      </div>

      <div class="contact__item" style="left:26px; top:329px;">
        <span class="contact__ring"></span>
        <span>@Reena_Yyc_Realtor</span>
      </div>
      <div class="contact__item" style="left:242px; top:329px;">
        <span class="contact__dot"></span>
        <span>RDhotRealty</span>
      </div>

      <div class="contact__item" style="left:107px; top:366px;">
        <svg class="contact__icon" viewBox="0 0 16 16"><path d="M1 8L8 1.5 15 8M3 6.5V15h4v-4h2v4h4V6.5M11 3V1.5h1.5v3"/></svg>
        <span>514 - 23 St NE | T3K5M8</span>
      </div>
    </div>
  </section>

  <section class="card card--back" aria-label="Card back">
    <h2 class="back__name">Reena Dhot</h2>
  </section>

</main>
</body>
</html>
```